Plakat-Design für Stellenanzeige für eine Allgemeinarztpraxis
Zielgruppe
Gemeinde Sonnhausen, ein kleine Landgemeinde im Nordosten von Baden-Württemberg mit ca. 3.600 Einwohner sucht für die ortsansässige Allgemeinarztpraxis einen Nachfolger*in. Die optimale Zielgruppe wären ja junge Ärzte - da sich dies wahrscheinlich als schwierig erweist wird an keine spezielle Altersgruppe gedacht.
Aufgabenstellung
Für die Bewerbung soll ein Straßenbanner im Bauzaunformat (340 x 0173 cm) erstellt werden.
Der Slogan könnte: 'Sonnhausen sucht einen Arzt' oder ähnlich lauten.
Ein modernes auffälliges Design wäre wünschenswert.

```html
<!DOCTYPE html>
<html lang="de">
<head>
<meta charset="utf-8">
<title>Sonnhausen sucht einen Arzt – Bauzaunbanner</title>
<link rel="stylesheet" href="https://fonts.googleapis.com/css2?family=Raleway:ital,wght@1,700;1,800&display=swap">
<style>
  :root {
    --stage: #dcdcdc;
    --banner: #f3f4f6;
    --band-blue: #5a88c3;
    --headline: #f3f3f3;
    --ink: #141414;
    --link-blue: #4d7dbf;
    --photo-light: #dfe6f1;
    --photo-mid: #9fb8dc;
    --photo-deep: #4f8cc4;
  }
  * { margin: 0; padding: 0; box-sizing: border-box; }
  html, body {
    width: 1200px;
    height: 864px;
    overflow: hidden;
    background: var(--stage);
    font-family: "Raleway", sans-serif;
  }
  .banner {
    position: absolute;
    left: 20px;
    top: 142px;
    width: 1160px;
    height: 580px;
    background: var(--banner);
    overflow: hidden;
  }
  .banner__photo {
    position: absolute;
    right: 0;
    top: 0;
    width: 640px;
    height: 100%;
    background:
      linear-gradient(90deg, var(--banner) 0%, rgba(243,244,246,0) 45%),
      linear-gradient(160deg, var(--photo-light) 0%, var(--photo-mid) 45%, var(--photo-deep) 70%, var(--photo-light) 100%);
  }
  .headline {
    position: absolute;
    left: 52px;
    top: 57px;
  }
  .headline__band {
    display: block;
    height: 103px;
    margin-bottom: 20px;
    background: var(--band-blue);
    color: var(--headline);
    font-style: italic;
    font-weight: 800;
    font-size: 96px;
    line-height: 100px;
    letter-spacing: -1px;
    padding-left: 50px;
    white-space: nowrap;
  }
  .headline__band--first { width: 608px; }
  .headline__band--second { width: 580px; padding-left: 44px; }
  .headline__band--third { width: 267px; padding-left: 42px; }
  .contact {
    position: absolute;
    left: 52px;
    top: 446px;
    font-style: italic;
    font-weight: 700;
    font-size: 36px;
    line-height: 46px;
    white-space: nowrap;
  }
  .contact__label { color: var(--ink); }
  .contact__url { color: var(--link-blue); }
</style>
</head>
<body>
  <main class="banner">
    <div class="banner__photo" role="img" aria-label="Foto: Ärztin im weißen Kittel mit Stethoskop, dahinter unscharf ein Ärzteteam"></div>
    <h1 class="headline">
      <span class="headline__band headline__band--first">Sonnhausen</span>
      <span class="headline__band headline__band--second">sucht einen</span>
      <span class="headline__band headline__band--third">Arzt</span>
    </h1>
    <p class="contact">
      <span class="contact__label">infos und bewerben unter:</span><br>
      <span class="contact__url">www.landpraxis-sonnhausen.de</span>
    </p>
  </main>
</body>
</html>
```